Wesbite design for Investment Firm

We want a basic (clean) website that follows the form, fonts and colors of our attachments. This is for a financial investment management firm, but we have a boutique (anti-Wall Street) approach. Site should have an Home Page (Logo up top - room for basic copy on bottom, Philosophy Page (room for Quarterly Letter attachment and basic copy, Performance Page (room for Performance Overview and Performance Analysis and basic copy), Team Page, Commentary Page and Contact
Updates

Reason: Some designers have asked for an extension. Again, please only use image of Train Station or Train Station Logo in design.

Target Market(s)

Small and mid-size financial advisors from across the country

Industry/Entity Type

Financial

Number of Pages Required

5+ page

Font styles to use
Other font styles liked:
• Palotino Linotype

Colors
3176b5
cfdeed
ffffff

Requirements
Must have
• Please refer to existing site www.qarvelton.com. Of note, this is too complex / cluttered. We simply want Blur, Grey and White consistent with attachments. The copy is pretty good, but will be simplified (and no quotes)
Should not have
• No images other than train station logo and / or train station image

```html
<!DOCTYPE html>
<html lang="en">
<head>
<meta charset="utf-8">
<title>Harrow Lane Investment Company</title>
<link rel="stylesheet" href="https://fonts.googleapis.com/css2?family=EB+Garamond:ital,wght@0,400;0,500;0,600;1,400;1,600&family=Open+Sans:wght@400;600&display=swap">
<style>
  :root {
    --blue: #3176b5;
    --navy: #1f3566;
    --pale: #e9eff7;
    --nav-bg: #eef2f7;
    --text: #4a4a4a;
    --muted: #666;
    --rule: #d3dbe6;
    --white: #ffffff;
  }
  * { box-sizing: border-box; margin: 0; padding: 0; }
  html, body { width: 845px; height: 1200px; overflow: hidden; background: var(--white); }
  body { position: relative; font-family: "Open Sans", Arial, sans-serif; color: var(--text); }

  /* Header */
  .site-header { position: absolute; top: 0; left: 0; width: 845px; height: 75px; }
  .social-dots { position: absolute; left: 78px; top: 22px; display: flex; gap: 4px; }
  .social-dots span {
    width: 25px; height: 25px; border-radius: 50%; border: 1.5px solid var(--navy);
    font-size: 5.5px; display: flex; align-items: center; justify-content: center; color: var(--navy);
  }
  .brand { position: absolute; left: 255px; top: 13px; width: 335px; text-align: center; }
  .brand-name {
    border-top: 1.5px solid var(--navy); border-bottom: 1.5px solid var(--navy);
    font-family: "EB Garamond", Georgia, serif; font-variant: small-caps; font-weight: 500;
    font-size: 23px; letter-spacing: 1px; color: var(--navy); line-height: 28px; padding-bottom: 1px;
  }
  .brand-tag { font-family: "EB Garamond", Georgia, serif; font-size: 12.5px; color: #555; margin-top: 3px; }
  .phone { position: absolute; right: 79px; top: 27px; font-size: 12px; color: var(--navy); display: flex; align-items: center; gap: 4px; }

  /* Navigation */
  .main-nav { position: absolute; top: 75px; left: 0; width: 845px; height: 31px; background: var(--nav-bg);
    display: flex; justify-content: center; align-items: center; gap: 30px; font-size: 12.5px; color: #333; }

  /* Hero */
  .hero { position: absolute; top: 106px; left: 0; width: 845px; height: 302px;
    background: linear-gradient(100deg, #3f7fc4 0%, #8fb3d8 18%, #e6e4df 35%, #d9d6cf 55%, #f1efea 72%, #4a6f45 88%, #2f5a8c 100%); }

  /* About */
  .about { position: absolute; top: 408px; left: 0; width: 845px; height: 320px; }
  .about-copy { position: absolute; left: 78px; top: 38px; width: 385px; }
  .section-title { font-family: "EB Garamond", Georgia, serif; font-variant: small-caps; font-weight: 600;
    font-size: 23px; color: var(--blue); letter-spacing: 0.6px; line-height: 1; }
  .about-copy p { font-size: 12.6px; line-height: 20.6px; margin-top: 10px; }
  .about-copy p + p { margin-top: 20px; }
  .about-divider { position: absolute; left: 472px; top: 40px; width: 1px; height: 240px; background: var(--rule); opacity: .6; }
  .quote { position: absolute; left: 490px; top: 35px; width: 276px; }
  .quote blockquote { font-family: "EB Garamond", Georgia, serif; font-style: italic; font-size: 19px;
    line-height: 24px; color: var(--blue); text-align: center; }
  .quote .mark { font-style: normal; font-weight: 600; font-size: 26px; line-height: 0; }
  .quote hr { border: 0; border-top: 1px solid var(--rule); margin: 14px 0 18px; }
  .quote cite { display: block; text-align: center; font-family: "EB Garamond", Georgia, serif; font-style: italic; color: var(--blue); }
  .quote .author { font-size: 23px; font-weight: 600; line-height: 1.1; }
  .quote .source { font-size: 14.5px; }

  /* Panels */
  .commentary { position: absolute; top: 728px; left: 0; width: 422px; height: 310px; background: var(--pale); text-align: center; }
  .commentary .section-title { margin-top: 34px; font-size: 22px; }
  .post-title { font-size: 14.5px; color: #222; margin-top: 17px; }
  .post-date { font-size: 10.5px; color: var(--muted); margin-top: 1px; }
  .post-excerpt { width: 265px; margin: 18px auto 0; font-size: 12.3px; line-height: 20.5px; }
  .btn { display: inline-block; margin-top: 19px; width: 95px; height: 30px; line-height: 30px;
    background: var(--blue); color: var(--white); font-size: 10.5px; border-radius: 1px; }
  .letter-panel { position: absolute; top: 728px; left: 422px; width: 423px; height: 310px; background: var(--blue); }
  .letter-panel .section-title { color: var(--white); margin: 34px 0 0 29px; font-size: 22px; }
  .letter-cover { position: absolute; left: 97px; top: 82px; width: 150px; height: 185px;
    background: linear-gradient(160deg, #ffffff, #e8ecf1); transform: rotate(8deg);
    box-shadow: -4px 3px 0 #f3f5f8; }

  /* Footer */
  .site-footer { position: absolute; top: 1038px; left: 0; width: 845px; height: 162px; }
  .footer-col { position: absolute; top: 34px; font-size: 9px; line-height: 12px; color: #333; }
  .footer-col h4 { font-size: 11px; font-weight: 600; color: var(--blue); margin-bottom: 7px; }
  .footer-col p + p { margin-top: 12px; }
  .links li { list-style: none; margin-bottom: 3.7px; }
  .footer-social { display: flex; gap: 4px; }
  .footer-social span { width: 27px; height: 27px; border-radius: 50%; border: 1.5px solid #555;
    font-size: 5.5px; display: flex; align-items: center; justify-content: center; color: #555; }
  .footer-brand { position: absolute; left: 607px; top: 40px; width: 160px; text-align: center; font-size: 8.8px; color: #444; }
  .footer-brand strong { font-family: "EB Garamond", Georgia, serif; font-weight: 600; font-size: 12.5px; color: var(--navy); display: block; }
  .footer-brand .tag { font-family: "EB Garamond", Georgia, serif; font-size: 7.5px; color: #666; }
  .footer-brand .legal { margin-top: 17px; line-height: 14px; }
</style>
</head>
<body>
  <header class="site-header">
    <div class="social-dots"><span>Linkora</span><span>Chirper</span><span>Circlet</span></div>
    <div class="brand">
      <div class="brand-name">Harrow Lane Investment Company</div>
      <div class="brand-tag">Separately Managed Accounts</div>
    </div>
    <div class="phone">
      <svg width="11" height="11" viewBox="0 0 24 24" aria-hidden="true"><path fill="#3176b5" d="M6.6 10.8a15.1 15.1 0 0 0 6.6 6.6l2.2-2.2c.3-.3.7-.4 1-.2 1.1.4 2.3.6 3.6.6.6 0 1 .4 1 1V20c0 .6-.4 1-1 1A17 17 0 0 1 3 4c0-.6.4-1 1-1h3.5c.6 0 1 .4 1 1 0 1.3.2 2.5.6 3.6.1.3 0 .7-.2 1z"/></svg>
      555.204.7318
    </div>
  </header>

  <nav class="main-nav">
    <span>Home</span><span>Philosophy</span><span>Performance</span><span>Team</span><span>Letters</span><span>Commentary</span><span>Contact</span>
  </nav>

  <div class="hero" role="img" aria-label="Photograph of a white clapboard train station under a blue sky with trees"></div>

  <section class="about">
    <div class="about-copy">
      <h2 class="section-title">Harrow Lane Investment Company</h2>
      <p>We founded Harrow Lane Investment Company in 1999, initially managing wealth from our family and friends in the town of Harrow Lane. The high expectations of our original investors is a key contributor to our value driven investment philosophy.</p>
      <p>Based in Dallas, TX, we manage assets for both individuals and institutions. Our investment methodology stresses absolute returns vs. relative performance, blending a combination of fundamental analysis, discipline and patience with the goal of preserving and compounding capital.</p>
    </div>
    <div class="about-divider"></div>
    <figure class="quote">
      <blockquote><span class="mark">&ldquo;</span> An investment operation is one which, upon thorough analysis, promises safety of principal and an adequate return. Operations not meeting these requirements are speculative. <span class="mark">&rdquo;</span></blockquote>
      <hr>
      <cite><span class="author">- Edmund Larkwell,</span><br><span class="source">The Patient Investor</span></cite>
    </figure>
  </section>

  <section class="commentary">
    <h2 class="section-title">Latest Commentary</h2>
    <h3 class="post-title">Core Equity Portfolio &ndash; Q2 2017</h3>
    <div class="post-date">August 10, 2017</div>
    <p class="post-excerpt">Based on our estimate of fair value relative to the company&rsquo;s current stock price, we determine each company&rsquo;s current margin of safety in the Core Equity.</p>
    <span class="btn">Read More</span>
  </section>

  <section class="letter-panel">
    <h2 class="section-title">Investment Adviser's Letter</h2>
    <div class="letter-cover" role="img" aria-label="Cover of the printed investment adviser's letter with a sketch of the train station"></div>
  </section>

  <footer class="site-footer">
    <div class="footer-col" style="left:78px">
      <h4>Contact us</h4>
      <p>1200 Cedar Brook Avenue,<br>Suite 410<br>Dallas, TX 75201</p>
      <p>555.204.7318<br>&nbsp;info@qarvelton.com</p>
    </div>
    <div class="footer-col" style="left:254px">
      <h4>Quick links</h4>
      <ul class="links">
        <li>Performance Overview</li>
        <li>Performance Analysis</li>
        <li>Verification Statement</li>
        <li>Harrow Lane ADV Part 2</li>
      </ul>
    </div>
    <div class="footer-col" style="left:431px">
      <h4>Social Media</h4>
      <div class="footer-social"><span>Linkora</span><span>Chirper</span><span>Circlet</span></div>
    </div>
    <div class="footer-brand">
      <strong>Harrow Lane Investment Company</strong>
      <span class="tag">Separately Managed Accounts</span>
      <div class="legal">&copy; 2017 Harrow Lane Investment Company<br>Terms of Use | Sitemap</div>
    </div>
  </footer>
</body>
</html>
```